Design a Flyer for Maple and Crest Cleaning

NEW VECTORISED LOGO'S ATTACHED!

Need a 2 sided, postcard sized flyer.
On one side I would like the logo (attached), and the web address)

On the main side, I require the following information:

info@[login to view URL]
07841592067

-Book in 60 seconds, Online, Easy
-Teams on 2 for double the clean
-No contracts
-Simple flat-rate pricing
-Fully insured
-On-time service
-We also support charities

10% off with code 'leaflet13'.

Please use the colors from the 2 designs attached

```html
<!DOCTYPE html>
<html lang="en">
<head>
<meta charset="utf-8">
<title>Maple and Crest Cleaning – Postcard Front</title>
<link rel="stylesheet" href="https://fonts.googleapis.com/css2?family=Arimo:wght@700&display=swap">
<style>
  :root {
    --blue-glow: #1ea4e6;
    --blue-mid: #0d63b4;
    --navy: #0a2760;
    --navy-band: #0d3a84;
    --sky-band: #1896da;
    --ink: #000000;
    --mark: #07142e;
    --white: #ffffff;
    --link-blue: #5a84d2;
  }
  html, body {
    margin: 0;
    padding: 0;
    width: 1200px;
    height: 845px;
    overflow: hidden;
    background: var(--ink);
  }
  .postcard {
    position: relative;
    width: 1200px;
    height: 845px;
    overflow: hidden;
    font-family: "Arimo", Arial, sans-serif;
  }
  .postcard__backdrop {
    position: absolute;
    inset: 0;
    width: 1200px;
    height: 845px;
  }
  .brand {
    position: absolute;
    left: 0;
    right: 0;
    top: 190px;
    display: flex;
    align-items: center;
    justify-content: center;
    gap: 40px;
  }
  .brand__square {
    width: 120px;
    height: 120px;
    background: var(--mark);
    flex: none;
  }
  .brand__name {
    margin: 0;
    color: var(--white);
    font-weight: 700;
    font-size: 80px;
    line-height: 1.05;
    letter-spacing: -0.5px;
    white-space: nowrap;
  }
  .web-address {
    position: absolute;
    left: 0;
    right: 0;
    top: 704px;
    margin: 0;
    text-align: center;
    color: var(--link-blue);
    font-weight: 700;
    font-size: 50px;
    letter-spacing: -0.5px;
  }
</style>
</head>
<body>
  <main class="postcard">
    <svg class="postcard__backdrop" viewBox="0 0 1200 845" aria-hidden="true">
      <defs>
        <radialGradient id="sky-glow" cx="620" cy="400" r="720" gradientUnits="userSpaceOnUse">
          <stop offset="0" stop-color="#1ea4e6"/>
          <stop offset="0.45" stop-color="#0d63b4"/>
          <stop offset="1" stop-color="#0a2760"/>
        </radialGradient>
      </defs>
      <rect class="backdrop__sky" x="0" y="0" width="1200" height="845" fill="url(#sky-glow)"/>
      <polygon class="backdrop__navy-band" points="0,590 1200,400 1200,465 0,625" fill="#0d3a84"/>
      <polygon class="backdrop__sky-band" points="0,625 1200,465 1200,515 0,690" fill="#1896da"/>
      <polygon class="backdrop__ground" points="0,690 1200,515 1200,845 0,845" fill="#000000"/>
    </svg>

    <div class="brand">
      <div class="brand__square" aria-hidden="true"></div>
      <h1 class="brand__name">Maple and Crest<br>Cleaning</h1>
    </div>

    <p class="web-address">www.MapleandCrest.com</p>
  </main>
</body>
</html>
```